Coastal Heritage Dairywrights' Guild needs new business cards

We need new business cards designed and produced. We are likely to need other design work done for ads, flyers etc in future.

We would like to start with an initial business card.

The Coastal Heritage Dairywrights' Guild (CHDG) is a membership-based not-for-profit organisation that looks after the interests of Australia's small to medium artisan cheesemakers, many of whom are also small-scale farmers. The design should be simple, using our logo, but also communicate our artisan cheese and small dairy farm focus.

The first card to be designed and produced is for me, Megan Thorburn. My details are:

Megan Thorburn
Secretary
Coastal Heritage Dairywrights' Guild (CHDG)
http://www.curdandcrockery.org
T +61427583914
E megan.meganthorburn@mailfern.net

I have attached the CHDG logo in jpg form. I have a higher resolution version available if needed.

Thank you!

Megan

Business

Megan Thorburn
Coastal Heritage Dairywrights' Guild
megan.meganthorburn@mailfern.net
+61427583914

Sans Serif

• Logo (see attached file)

```html
<!DOCTYPE html>
<html lang="en">
<head>
<meta charset="utf-8">
<title>Coastal Heritage Dairywrights' Guild — Business Cards</title>
<link href="https://fonts.googleapis.com/css2?family=Sorts+Mill+Goudy&family=Montserrat:wght@400;600&display=swap" rel="stylesheet">
<style>
  :root {
    --stage: #3a3a3a;
    --brown: #4a2708;
    --ink: #4f2a0c;
    --cheese: #f2c25a;
    --paper: #ffffff;
    --muted: #7d7d7d;
    --cream: #ffffff;
  }
  html, body {
    margin: 0;
    width: 1200px;
    height: 855px;
    overflow: hidden;
    background: var(--stage);
  }
  .canvas {
    position: relative;
    width: 1200px;
    height: 855px;
  }
  .card {
    position: absolute;
    width: 560px;
    height: 320px;
    overflow: hidden;
    box-shadow: 0 10px 30px rgba(0,0,0,.45);
  }
  .card--front { left: 60px; top: 80px; background: var(--brown); }
  .card--back  { left: 580px; top: 455px; background: var(--paper); }

  .brand {
    position: absolute;
    display: flex;
    align-items: center;
    gap: 18px;
  }
  .brand__dot {
    flex: none;
    border-radius: 50%;
    background: var(--cheese);
  }
  .brand__name {
    font-family: "Sorts Mill Goudy", Georgia, serif;
    line-height: 1.02;
    letter-spacing: .5px;
  }
  .card--front .brand { left: 130px; top: 95px; }
  .card--front .brand__dot { width: 56px; height: 56px; }
  .card--front .brand__name { color: var(--cream); font-size: 27px; }

  .card--back .brand { left: 34px; top: 112px; gap: 12px; }
  .card--back .brand__dot { width: 40px; height: 40px; }
  .card--back .brand__name { color: var(--ink); font-size: 20px; letter-spacing: .3px; }

  .divider {
    position: absolute;
    left: 262px;
    top: 100px;
    width: 2px;
    height: 112px;
    background: var(--ink);
  }
  .person {
    position: absolute;
    left: 280px;
    top: 104px;
    width: 264px;
    font-family: "Montserrat", Arial, sans-serif;
  }
  .person__name {
    margin: 0;
    font-size: 20px;
    font-weight: 600;
    color: var(--ink);
  }
  .person__role {
    margin: 2px 0 22px;
    font-size: 12px;
    color: var(--muted);
  }
  .contact {
    list-style: none;
    margin: 0;
    padding: 0;
    font-size: 12px;
    color: var(--muted);
  }
  .contact li {
    display: flex;
    align-items: center;
    gap: 7px;
    margin-bottom: 5px;
    white-space: nowrap;
  }
  .contact svg { width: 11px; height: 11px; fill: var(--ink); flex: none; }
</style>
</head>
<body>
<main class="canvas">
  <section class="card card--front">
    <div class="brand">
      <span class="brand__dot"></span>
      <div class="brand__name">Coastal Heritage<br>Dairywrights'<br>Guild</div>
    </div>
  </section>

  <section class="card card--back">
    <div class="brand">
      <span class="brand__dot"></span>
      <div class="brand__name">Coastal Heritage<br>Dairywrights'<br>Guild</div>
    </div>
    <span class="divider"></span>
    <div class="person">
      <h1 class="person__name">Megan Thorburn</h1>
      <p class="person__role">Secretary</p>
      <ul class="contact">
        <li>
          <svg viewBox="0 0 24 24" aria-hidden="true"><path d="M6.6 10.8a15 15 0 0 0 6.6 6.6l2.2-2.2c.3-.3.7-.4 1-.2 1.1.4 2.3.6 3.6.6.6 0 1 .4 1 1V20c0 .6-.4 1-1 1A17 17 0 0 1 3 4c0-.6.4-1 1-1h3.5c.6 0 1 .4 1 1 0 1.3.2 2.5.6 3.6.1.3 0 .7-.2 1z"/></svg>
          <span>+61427583914</span>
        </li>
        <li>
          <svg viewBox="0 0 24 24" aria-hidden="true"><path d="M2 5h20v14H2zm2 2v.5l8 5 8-5V7zm0 3v7h16v-7l-8 5z"/></svg>
          <span>megan.meganthorburn@mailfern.net</span>
        </li>
      </ul>
    </div>
  </section>
</main>
</body>
</html>
```